Need Business Card for our Real Estate Business with Sales Executive's Picture

PANTONE 484 C ( RED)

PANTONE 2766 C ( BLUE

Industry/Entity Type

Real Estate

Contact Information for Business Card

Name, Mobile, email, & picture of Person
Agency Phone, address, Web address

Requirements
Must have
• Our Logo Colours, Agent Picture,

```html
<!DOCTYPE html>
<html lang="en">
<head>
<meta charset="utf-8">
<title>Marlowe Real Estate – Business Card</title>
<link rel="stylesheet" href="https://fonts.googleapis.com/css2?family=EB+Garamond:wght@400;500;600&display=swap">
<style>
  :root {
    --navy: #0f1d5a;
    --navy-deep: #0a1544;
    --red: #8e1b26;
    --white: #ffffff;
    --stage: #e4e1dc;
    --ink: #1a2a6c;
    --text: #2a2a3a;
  }
  * { box-sizing: border-box; margin: 0; padding: 0; }
  html, body { width: 1200px; height: 780px; overflow: hidden; }
  body {
    background: var(--stage);
    font-family: "EB Garamond", Georgia, serif;
    position: relative;
  }
  .card {
    position: absolute;
    width: 540px;
    height: 309px;
    top: 236px;
    overflow: hidden;
    background: var(--navy);
    box-shadow: 0 10px 28px rgba(0,0,0,0.22);
  }
  .card--front { left: 40px; }
  .card--back {
    left: 620px;
    background: radial-gradient(ellipse at 50% 45%, #13246a 0%, var(--navy-deep) 100%);
  }

  .front-top {
    position: absolute; left: 0; top: 0; width: 100%; height: 170px;
    background: linear-gradient(160deg, #13246a 0%, var(--navy) 70%);
  }
  .front-info {
    position: absolute; left: 0; top: 170px; width: 100%; height: 95px;
    background: var(--white);
  }
  .web-band {
    position: absolute; left: 0; bottom: 0; width: 100%; height: 44px;
    background: var(--red);
    display: flex; align-items: center;
    color: var(--white);
    font-size: 13px; letter-spacing: 4px; text-transform: uppercase;
  }
  .card--front .web-band { padding-left: 56px; }
  .card--back .web-band { justify-content: center; }

  .agent-photo {
    position: absolute; right: 0; top: 18px; width: 250px; height: 222px;
    background: linear-gradient(200deg, #2f55b8 0%, #1c3a8e 55%, #dfe3ee 100%);
  }
  .photo-edge {
    position: absolute; right: 0; top: 0; width: 120px; height: 18px;
    background: var(--white);
  }

  .brand-name {
    position: absolute;
    color: var(--white);
    font-weight: 500;
    letter-spacing: 1px;
    white-space: nowrap;
  }
  .card--front .brand-name { left: 44px; top: 68px; font-size: 28px; }
  .card--back .brand-name {
    left: 50%; top: 112px; transform: translateX(-50%); font-size: 36px;
  }

  .contact { position: absolute; left: 44px; top: 178px; color: var(--ink); }
  .contact__name { font-size: 17px; font-weight: 600; letter-spacing: 1px; text-transform: uppercase; line-height: 1.1; }
  .contact__role { font-size: 13px; color: var(--red); margin-bottom: 4px; }
  .contact__line { font-size: 12px; line-height: 1.35; color: var(--text); }
  .contact__label { color: var(--red); font-weight: 600; }
  .sep { color: #999; margin: 0 4px; }
</style>
</head>
<body>
  <section class="card card--front" aria-label="Business card front">
    <div class="front-top"></div>
    <div class="front-info"></div>
    <div class="photo-edge"></div>
    <div class="agent-photo" role="img" aria-label="Portrait photo of the agent in a blue suit"></div>

    <p class="brand-name">Marlowe Real Estate</p>

    <div class="contact">
      <p class="contact__name">Daniel Carver</p>
      <p class="contact__role">Owner</p>
      <p class="contact__line"><span class="contact__label">M:</span> (555) 014-2280<span class="sep">|</span><span class="contact__label">E:</span> hello@marlowehomes.com</p>
      <p class="contact__line"><span class="contact__label">A:</span> PO Box 418, 14 Quay Lane, Melbourne</p>
    </div>

    <div class="web-band">www.marlowehomes.com</div>
  </section>

  <section class="card card--back" aria-label="Business card back">
    <p class="brand-name">Marlowe Real Estate</p>
    <div class="web-band">www.marlowehomes.com</div>
  </section>
</body>
</html>
```